Australian Real Estate Sales Consultant needs web design please.

I am a female residential real estate sales consultant for a large australian real estate franchise.
I need a web design for "wordpress" that contains an area that will accommodate my photo and details and company logo.
A large area that contains a feature property where images are on something like a slide show.
Tabs or something similar with images for Selling, Sold, Photography and News where people can look at listings but I do not want people to be able to post a comment.
Reason: Need more designers, may be forced to change to wordpress and offer more money.
Reason: Sorry for the delay, I have been concentrating on another project which I needed completed. I am now able to focus on my web design project and hope to have it all set up in the next 10 days as it is a high priority for me. Thank you for your patience and I will begin providing feedback to your designs shortly. Thanks, Marisha.
Target Market(s)
Potential sellers or purchasers of residential property
Industry/Entity Type
Residential
Requirements
Must have
- Ease of changing property photos and info
Nice to have
- Bright attractive colours

```html
<!DOCTYPE html>
<html lang="en">
<head>
<meta charset="utf-8">
<title>Marisha Kestrel – Residential Sales Consultant</title>
<link href="https://fonts.googleapis.com/css2?family=Arimo:wght@400;700&family=Yanone+Kaffeesatz:wght@400;500&display=swap" rel="stylesheet">
<style>
:root{
  --backdrop:#e4e4e4;
  --page:#ffffff;
  --ink:#333333;
  --body-text:#4a4a4a;
  --navy:#0f3a7a;
  --brand-blue:#1a4f9c;
  --nav-top:#1d58a8;
  --nav-bottom:#0c3478;
  --nav-divider:#0a2d66;
  --red:#d8232a;
  --red-dark:#a8141a;
  --slide-dark:#04112b;
  --slide-mid:#0b2e6b;
  --slide-accent:#2aa3ff;
  --rule:#dddddd;
}
*{box-sizing:border-box;margin:0;padding:0}
html,body{width:1200px;height:800px;overflow:hidden}
body{
  background:linear-gradient(90deg,#d9d9d9 0,#eeeeee 8%,#eeeeee 92%,#d9d9d9 100%);
  font-family:"Arimo",Arial,sans-serif;color:var(--ink);position:relative;
}
.page{
  position:absolute;left:98px;top:0;width:1004px;height:800px;
  background:var(--page);box-shadow:0 0 8px rgba(0,0,0,.35);
}
.call-label{position:absolute;left:20px;top:19px;font-size:17px;font-weight:700;color:#2b2b2b;letter-spacing:.2px}
.call-number{position:absolute;left:20px;top:42px;display:flex;align-items:center;gap:6px;font-size:24px;font-weight:700;color:var(--brand-blue)}
.brand{position:absolute;left:717px;top:27px;height:34px;display:flex;align-items:center;gap:10px;font-size:22px;font-weight:700;color:var(--navy)}
.brand-square{width:26px;height:26px;background:var(--red)}

.slider{
  position:absolute;left:20px;top:87px;width:963px;height:218px;border-radius:4px;overflow:hidden;
  background:radial-gradient(ellipse at 30% 50%,var(--slide-mid) 0,var(--slide-dark) 75%);
}
.slider-photo{
  position:absolute;left:392px;top:0;width:571px;height:218px;
  background:linear-gradient(180deg,#3d79c4 0,#9cc3ea 45%,#d8dde2 70%,#3f8f2c 100%);
}
.slider-photo::before{content:"";position:absolute;left:0;top:0;width:140px;height:100%;background:linear-gradient(90deg,var(--slide-dark),rgba(4,17,43,0))}
.slide-name{position:absolute;left:78px;top:28px;font-family:"Yanone Kaffeesatz",sans-serif;font-size:50px;font-weight:400;color:#fff;line-height:1}
.slide-tagline{position:absolute;left:79px;top:88px;font-family:"Yanone Kaffeesatz",sans-serif;font-size:27px;line-height:27px;color:var(--slide-accent)}
.btn-read{
  position:absolute;left:82px;top:162px;width:85px;height:25px;border-radius:4px;
  background:linear-gradient(#ffffff,#c9cdd2);border:1px solid #8c939b;
  font-size:11.5px;font-weight:700;color:#333;text-align:center;line-height:23px;
}
.arrow{position:absolute;top:82px}
.arrow-prev{left:8px}
.arrow-next{right:6px}

.main-nav{
  position:absolute;left:20px;top:322px;width:963px;height:38px;border-radius:4px;
  background:linear-gradient(var(--nav-top),var(--nav-bottom));display:flex;align-items:stretch;
}
.main-nav a{
  color:#fff;text-decoration:none;font-size:13px;font-weight:700;
  display:flex;align-items:center;padding:0 15px;border-right:1px solid var(--nav-divider);
}
.main-nav a.active{background:linear-gradient(#ee2f35,var(--red-dark));border-radius:4px 0 0 4px;padding:0 14px 0 15px}
.search{
  position:absolute;right:10px;top:9px;width:181px;height:21px;border-radius:5px;background:#fff;
  border:1px solid #9aa7b8;font-size:12px;color:#777;padding:3px 0 0 7px;
}
.search svg{position:absolute;right:5px;top:3px}

.section-title{font-family:"Yanone Kaffeesatz",sans-serif;font-weight:400;font-size:27px;line-height:1;letter-spacing:.3px}
.for-sale-title{position:absolute;left:29px;top:387px;color:var(--red)}
.listings{position:absolute;left:30px;top:424px;display:flex;gap:19px}
.listing{width:222px}
.listing-photo{width:222px;height:126px;border-radius:4px}
.photo-white{background:linear-gradient(180deg,#4f8fd6 0,#b7d3ee 40%,#e9ecef 62%,#4c9a2f 88%)}
.photo-timber{background:linear-gradient(180deg,#7aa6d4 0,#c9b48a 35%,#a8875a 70%,#6b8a4a 100%)}
.listing p{margin-top:10px;padding-left:2px;font-size:12.5px;line-height:20px;color:var(--body-text)}
.listing a{color:var(--navy)}

.welcome{position:absolute;left:51px;top:695px;width:580px}
.welcome .section-title,.news .section-title{color:var(--navy)}
.title-rule{height:1px;margin-top:4px;width:275px;background:linear-gradient(90deg,var(--rule),rgba(221,221,221,0))}
.welcome p{margin-top:13px;font-size:12.5px;line-height:20px;color:var(--body-text)}
.column-divider{position:absolute;left:647px;top:705px;width:1px;height:95px;background:var(--rule)}
.news{position:absolute;left:672px;top:695px;width:300px}
.news .title-rule{width:115px}
.news h3{margin-top:12px;font-size:12.5px;font-weight:700;color:#444}
.news .meta{font-size:12px;color:#555;margin-top:4px}
.news p{font-size:12.5px;line-height:20px;color:var(--body-text);margin-top:2px}
</style>
</head>
<body>
<div class="page">
  <header>
    <div class="call-label">CALL US NOW</div>
    <div class="call-number">
      <svg width="30" height="28" viewBox="0 0 30 28" aria-hidden="true">
        <path d="M3 14a12 12 0 0 1 22-7" fill="none" stroke="#8c1a1e" stroke-width="2"/>
        <path d="M9 5c-2 0-4 2-4 5 0 7 6 14 13 15 3 0 5-2 5-4l-4-3-3 2c-3-1-6-5-7-8l2-3z" fill="var(--red)"/>
      </svg>
      <span>012-555-0189</span>
    </div>
    <div class="brand"><span class="brand-square"></span>Harbourline Realty</div>
  </header>

  <section class="slider">
    <div class="slider-photo" role="img" aria-label="Portrait of the consultant beside a white two-storey house under a blue sky"></div>
    <h1 class="slide-name">Marisha Kestrel</h1>
    <p class="slide-tagline">I am a female residential real estate<br>sales consultant...</p>
    <a class="btn-read">READ MORE</a>
    <svg class="arrow arrow-prev" width="42" height="46" viewBox="0 0 42 46" aria-hidden="true"><path d="M30 2 8 23l22 21" fill="none" stroke="rgba(190,190,190,.55)" stroke-width="8"/></svg>
    <svg class="arrow arrow-next" width="42" height="46" viewBox="0 0 42 46" aria-hidden="true"><path d="M12 2l22 21-22 21" fill="none" stroke="rgba(220,220,220,.7)" stroke-width="8"/></svg>
  </section>

  <nav class="main-nav">
    <a class="active">Home</a><a>Selling</a><a>Sold</a><a>Photography</a><a>About Me</a><a>Contact</a><a>Testimonials</a><a style="border-right:0">News</a>
    <div class="search">Search Here
      <svg width="16" height="14" viewBox="0 0 16 14" aria-hidden="true"><circle cx="6" cy="6" r="4.5" fill="none" stroke="#444" stroke-width="1.6"/><path d="M9.5 9l5 4" stroke="#444" stroke-width="2"/></svg>
    </div>
  </nav>

  <h2 class="section-title for-sale-title">PROPERTIES FOR SALE</h2>
  <div class="listings">
    <article class="listing">
      <div class="listing-photo photo-white" role="img" aria-label="White weatherboard house with a for sale sign on the lawn"></div>
      <p>Lorem ipsum dolor sit amet, consecte<br>tur adipiscing elit. Etiam a turpis nutk<br>sodales adipiscing. Clamcorper seed<br>nibh. Cras fermentum eleifend mollis.<br>Vestibulum... (<a>Read More</a>)</p>
    </article>
    <article class="listing">
      <div class="listing-photo photo-timber" role="img" aria-label="Timber-clad two-storey house with a front porch"></div>
      <p>Lorem ipsum dolor sit amet, consecte<br>tur adipiscing elit. Etiam a turpis nutk<br>sodales adipiscing. Clamcorper seed<br>nibh. Cras fermentum eleifend mollis.<br>Vestibulum... (<a>Read More</a>)</p>
    </article>
    <article class="listing">
      <div class="listing-photo photo-white" role="img" aria-label="White weatherboard house with a for sale sign on the lawn"></div>
      <p>Lorem ipsum dolor sit amet, consecte<br>tur adipiscing elit. Etiam a turpis nutk<br>sodales adipiscing. Clamcorper seed<br>nibh. Cras fermentum eleifend mollis.<br>Vestibulum... (<a>Read More</a>)</p>
    </article>
    <article class="listing">
      <div class="listing-photo photo-timber" role="img" aria-label="Timber-clad two-storey house with a front porch"></div>
      <p>Lorem ipsum dolor sit amet, consecte<br>tur adipiscing elit. Etiam a turpis nutk<br>sodales adipiscing. Clamcorper seed<br>nibh. Cras fermentum eleifend mollis.<br>Vestibulum... (<a>Read More</a>)</p>
    </article>
  </div>

  <section class="welcome">
    <h2 class="section-title">WELCOME TO OUR WEBSITE</h2>
    <div class="title-rule"></div>
    <p>Lorem ipsum dolor sit amet, consectetur adipiscing elit. Etiam a turpis non odio sodales adipiscing.<br>Cras nibh nisl, luctus eu ornare eu, ullamcorper sed nibh. Cras fermentum eleifend mollis. Vestib<br>ulum ac gra vida nunc. Praesent elementum tortor et magna aliquet sit amet condimentum orci<br>blandit. Etiam tortor sed consequat aliquet nulla pellentesque.</p>
  </section>
  <div class="column-divider"></div>
  <aside class="news">
    <h2 class="section-title">NEWS</h2>
    <div class="title-rule"></div>
    <h3>Lorem ipsum dolor sit amet</h3>
    <div class="meta">Posted by Admin on 1st October.</div>
    <p>Consectetur adipiscing elit tiam a turpis non odio<br>sodales nec nibh luctus eu ornare.</p>
  </aside>
</div>
</body>
</html>
```